Corvallin Property Solutions need a business card design

Hello guys. We would need a business card design asap please.
We are a start up property investment business based in London UK specialised in buying, selling, managing and letting properties and helping distressed property owners.
The name of our Business is Corvallin, the logo symbolises the four fundamental elements of the world (earth, air, fire and water) and so it stands for strength, stability, longevity.
We would like the business card to communicate professionalism and reliability. Many many thanks indeed for your work.

Details:

1.) Marisol Dunkley
Property Investor
Mobile: +44(0)7700362517
Email: marisol.corvallin@quilbrook.example

2.) Tomas Brindle
Property Investor
Mobile: +44(0)7700845926
Email: tomas.corvallin@quilbrook.example

Industry/Entity Type

Investment

```html
<!DOCTYPE html>
<html lang="en">
<head>
<meta charset="utf-8">
<title>Corvallin Property Solutions – Business Card</title>
<link href="https://fonts.googleapis.com/css2?family=Montserrat:wght@300;400;600;700;900&display=swap" rel="stylesheet">
<style>
  :root {
    --backdrop: #7a7a7a;
    --card: #ffffff;
    --ink: #111111;
    --red: #e61e2d;
    --green: #00872f;
    --blue: #005bcc;
  }
  html, body {
    margin: 0;
    padding: 0;
    width: 1038px;
    height: 1200px;
    overflow: hidden;
    background: var(--backdrop);
  }
  .canvas {
    position: relative;
    width: 1078px;
    height: 1246px;
    transform: scale(0.9629);
    transform-origin: 0 0;
    font-family: "Montserrat", Arial, sans-serif;
    color: var(--ink);
  }
  .card {
    position: absolute;
    left: 14px;
    width: 1050px;
    height: 599px;
    background: var(--card);
    box-shadow: 0 4px 14px rgba(0,0,0,0.45);
    overflow: hidden;
  }
  .card--front { top: 16px; }
  .card--back { top: 630px; }
  .card__bands {
    position: absolute;
    inset: 0;
    width: 100%;
    height: 100%;
  }
  .band--red { fill: var(--red); }
  .band--green { fill: var(--green); }
  .band--blue { fill: var(--blue); }

  .brand {
    position: absolute;
    text-align: center;
    font-weight: 700;
    color: var(--ink);
    line-height: 1;
    text-transform: uppercase;
  }
  .brand__name { display: block; letter-spacing: 0.5px; }
  .brand__tagline { display: block; }

  .card--front .brand { left: 0; right: 0; top: 385px; }
  .card--front .brand__name { font-size: 46px; }
  .card--front .brand__tagline { font-size: 21px; margin-top: 16px; }

  .front__email {
    position: absolute;
    left: 0; right: 0;
    top: 551px;
    text-align: center;
    font-size: 20px;
    font-weight: 400;
    letter-spacing: 0.3px;
  }

  .card--back .brand { left: 56px; width: 260px; top: 248px; }
  .card--back .brand__name { font-size: 28px; }
  .card--back .brand__tagline { font-size: 14px; margin-top: 10px; }

  .person {
    position: absolute;
    left: 343px;
    width: 500px;
    top: 220px;
    text-align: center;
    line-height: 1;
  }
  .person__name {
    margin: 0;
    font-size: 42px;
    font-weight: 900;
    letter-spacing: 0.5px;
    text-transform: uppercase;
  }
  .person__role {
    margin: 10px 0 0;
    font-size: 31px;
    font-weight: 300;
    text-transform: uppercase;
  }

  .contact {
    position: absolute;
    right: 76px;
    top: 442px;
    text-align: right;
    font-size: 30px;
    font-weight: 400;
    line-height: 42px;
    list-style: none;
    margin: 0;
    padding: 0;
  }
  .contact__item { display: flex; align-items: center; justify-content: flex-end; gap: 10px; }
  .contact__icon { width: 24px; height: 24px; fill: var(--ink); }
  .contact__icon--mail { width: 30px; height: 22px; }
</style>
</head>
<body>
<div class="canvas">

  <section class="card card--front">
    <svg class="card__bands" viewBox="0 0 1050 599" aria-hidden="true">
      <polygon class="band--red" points="429,0 543,0 429,199"/>
      <polygon class="band--green" points="0,200 429,200 366,313 0,313"/>
      <polygon class="band--blue" points="622,200 1050,200 1050,313 684,313"/>
    </svg>
    <div class="brand">
      <span class="brand__name">Corvallin</span>
      <span class="brand__tagline">Property Solutions</span>
    </div>
    <div class="front__email">MARISOL.CORVALLIN@QUILBROOK.EXAMPLE</div>
  </section>

  <section class="card card--back">
    <svg class="card__bands" viewBox="0 0 1050 599" aria-hidden="true">
      <polygon class="band--red" points="608,0 721,0 608,195"/>
      <polygon class="band--green" points="0,334 527,334 463,447 0,447"/>
      <polygon class="band--blue" points="908,298 1050,298 1050,411 973,411"/>
    </svg>
    <div class="brand">
      <span class="brand__name">Corvallin</span>
      <span class="brand__tagline">Property Solutions</span>
    </div>
    <div class="person">
      <h1 class="person__name">Marisol Dunkley</h1>
      <p class="person__role">Property Investor</p>
    </div>
    <ul class="contact">
      <li class="contact__item">
        <svg class="contact__icon" viewBox="0 0 24 24" aria-hidden="true"><path d="M6.6 10.8c1.4 2.8 3.8 5.1 6.6 6.6l2.2-2.2c.3-.3.7-.4 1-.2 1.1.4 2.3.6 3.6.6.6 0 1 .4 1 1V20c0 .6-.4 1-1 1C10.6 21 3 13.4 3 4c0-.6.4-1 1-1h3.5c.6 0 1 .4 1 1 0 1.3.2 2.5.6 3.6.1.3 0 .7-.2 1l-2.3 2.2z"/></svg>
        <span>+44(0)7700362517</span>
      </li>
      <li class="contact__item">
        <svg class="contact__icon contact__icon--mail" viewBox="0 0 30 22" aria-hidden="true"><path d="M0 0h30v22H0z M2 2v1l13 9 13-9V2z M2 5.5V20h26V5.5L15 14.5z" fill-rule="evenodd"/></svg>
        <span>MARISOL.CORVALLIN@QUILBROOK.EXAMPLE</span>
      </li>
    </ul>
  </section>

</div>
</body>
</html>
```